We are looking to recreate our Harmon & Company Jobsite Sign. This sign will be placed by the street at each of our jobsites. We want to keep this sign simple, but at the same time, want to add a catching appeal to the design for anyone passing by. We want to stick to a two color scheme (Harmon Blue, and White). Please only use the Company Logo that I have uploaded for this project. Please also see a mock up of what we would like to include on this sign. The Sign Dimensions will be 4' x 8'. Please keep all verbiage uniform with the verbiage on the sample design I have uploaded. LET YOUR CREATIVITY FLOW!

```html
<!DOCTYPE html>
<html lang="en">
<head>
<meta charset="utf-8">
<title>Harmon &amp; Company Jobsite Sign</title>
<link href="https://fonts.googleapis.com/css2?family=Alegreya:wght@500;600;700;800&display=swap" rel="stylesheet">
<style>
  :root {
    --harmon-blue: #16198f;
    --harmon-blue-light: #1a1d97;
    --white: #ffffff;
    --backdrop: #c9c9c9;
  }
  html, body {
    margin: 0;
    padding: 0;
    width: 1089px;
    height: 1200px;
    overflow: hidden;
    background: var(--backdrop);
  }
  p { margin: 0; }
  .sign {
    position: absolute;
    left: 91px;
    top: 373px;
    width: 907px;
    height: 453px;
    font-family: "Alegreya", Georgia, serif;
    color: var(--white);
    overflow: hidden;
  }
  .sign-shapes {
    position: absolute;
    inset: 0;
    width: 907px;
    height: 453px;
  }
  .brand {
    position: absolute;
    right: 471px;
    top: 34px;
    text-align: right;
    font-weight: 800;
    line-height: 1;
  }
  .brand-name {
    display: block;
    font-size: 78px;
    letter-spacing: -1px;
  }
  .brand-suffix {
    display: block;
    font-size: 36px;
    margin-top: -4px;
  }
  .brand-divider {
    position: absolute;
    left: 448px;
    top: 42px;
    width: 3px;
    height: 113px;
    background: var(--white);
  }
  .services {
    position: absolute;
    left: 460px;
    top: 40px;
    width: 368px;
    text-align: center;
    font-weight: 700;
    font-size: 62px;
    line-height: 0.86;
  }
  .tagline {
    position: absolute;
    left: 0;
    top: 180px;
    width: 907px;
    text-align: center;
    font-weight: 700;
    font-size: 40px;
    line-height: 1;
  }
  .location {
    position: absolute;
    left: 0;
    top: 225px;
    width: 907px;
    text-align: center;
    font-weight: 700;
    font-size: 29px;
    line-height: 1;
  }
  .location .rule {
    display: inline-block;
    width: 28px;
    height: 2px;
    background: var(--white);
    vertical-align: 8px;
    margin: 0 12px;
  }
  .license {
    position: absolute;
    left: 0;
    top: 264px;
    width: 907px;
    text-align: center;
    font-weight: 600;
    font-size: 21px;
    line-height: 1;
    letter-spacing: 0.5px;
  }
  .website {
    position: absolute;
    left: 239px;
    top: 385px;
    font-weight: 700;
    font-size: 37px;
    line-height: 1;
    color: var(--harmon-blue);
  }
  .phone {
    position: absolute;
    left: 636px;
    top: 382px;
    font-weight: 600;
    font-size: 42px;
    line-height: 1;
    color: var(--harmon-blue);
  }
</style>
</head>
<body>
  <main class="sign">
    <svg class="sign-shapes" viewBox="0 0 1524 762" preserveAspectRatio="none">
      <rect class="panel" x="0" y="0" width="1524" height="762" fill="var(--harmon-blue)"/>
      <rect class="skyline-backdrop" x="347" y="120" width="820" height="450" fill="var(--harmon-blue-light)" role="img" aria-label="Faint outline drawing of a city skyline behind the sign text"/>
      <polygon class="swoosh-stripe" points="0,473 1524,630 0,489" fill="var(--white)"/>
      <polygon class="footer-band" points="0,545 1524,626 1524,762 0,762" fill="var(--white)"/>
      <g class="social-links" fill="none" stroke="var(--harmon-blue)" stroke-width="4">
        <circle cx="97" cy="678" r="30"/>
        <circle cx="174" cy="678" r="30"/>
        <circle cx="250" cy="678" r="30"/>
      </g>
    </svg>

    <div class="brand">
      <span class="brand-name">Harmon</span>
      <span class="brand-suffix">&amp; Company, Inc.</span>
    </div>
    <div class="brand-divider"></div>
    <div class="services">General<br>Contractors</div>

    <p class="tagline">“Building Trust On Every Site”</p>
    <p class="location"><span class="rule"></span>Cedar Grove, Florida<span class="rule"></span></p>
    <p class="license">CGC1472583</p>

    <div class="website">HarmonCompany.net</div>
    <div class="phone">407-555-0148</div>
  </main>
</body>
</html>
```